Marketplace for construction material and human resources

I need to create a portal for construction companies in Qatar (and then expand ) to be able to sell their stored materials and buy stored materials and let other companies what human resources (labor force) they are releasing and allow companies to search for human resources to acquire that are up for release from other companies.
Please look at the attached excel sheet.
Updates

Multiple requests for an extension however i will select on a first preference basis, i will not wait till the end of the period, if we find a design we like and a designer that is fit for our project!

Target Market(s)

Construction Companies

Logo Text

Construction Material & Resources

Coding

Coded - Design and coding required

Number of Pages Required

5+ page

Font styles to use
Sans Serif

Requirements
Must have
• A portal to register as a company, including a verification process from our team and membership fees. A portal to list stored material that are for sale. A search mechanism for users to search and purchase material listed. A mechanism to list released man power and a mechanism to search and acquire available man power.

```html
<!DOCTYPE html>
<html lang="en">
<head>
<meta charset="utf-8">
<title>STRATA Qatar – Construction Material &amp; Resources</title>
<link href="https://fonts.googleapis.com/css2?family=IBM+Plex+Sans:wght@400;500;600;700&family=Montserrat:wght@800;900&family=Oswald:wght@500&display=swap" rel="stylesheet">
<style>
:root{
  --orange:#e0961c;
  --ink:#222222;
  --text:#444444;
  --muted:#666666;
  --soft:#f4f0f0;
  --line:#d9d9d9;
  --footer:#222224;
  --white:#ffffff;
}
*{box-sizing:border-box;margin:0;padding:0}
html,body{width:1200px;height:3479px;overflow:hidden}
body{position:relative;font-family:"IBM Plex Sans",sans-serif;color:var(--text);background:var(--white)}
.abs{position:absolute}
a{color:inherit;text-decoration:none}

/* header */
.site-header{position:absolute;left:0;top:0;width:1200px;height:110px;background:var(--white)}
.brand{position:absolute;display:flex;align-items:center;gap:10px}
.brand-mark{width:34px;height:34px;background:var(--orange)}
.brand-name{font-family:"IBM Plex Sans",sans-serif;font-weight:600;color:var(--ink);font-size:30px;letter-spacing:1px;line-height:1}
.brand-name small{display:block;font-size:13px;letter-spacing:4px;text-align:right;margin-top:2px;font-weight:600}
.search-top{left:516px;top:23px;width:234px;height:31px;border:1px solid #333;font-size:9px;color:#333;padding:9px 10px}
.search-top svg{position:absolute;right:8px;top:8px}
.btn-register{left:765px;top:23px;width:94px;height:31px;background:var(--orange);color:#fff;font-size:12px;font-weight:500;display:flex;align-items:center;justify-content:center;letter-spacing:.5px}
.lang{left:877px;top:23px;width:77px;height:31px;border:1px solid #aaa;font-size:11px;display:flex;align-items:center;gap:6px;padding-left:9px;color:#333}
.flag{width:20px;height:12px;background:#2b3f86;position:relative}
.cart{left:977px;top:24px;font-size:10px;color:#333;display:flex;align-items:flex-end;gap:4px}
.cart-badge{position:absolute;left:73px;top:-3px;width:17px;height:17px;border-radius:50%;background:var(--orange);color:#fff;font-size:10px;display:flex;align-items:center;justify-content:center}
.main-nav{left:517px;top:77px;display:flex;font-size:13.5px;font-weight:600;color:var(--ink)}
.main-nav a{margin-right:33px}
.main-nav a:last-child{margin-right:0}
.main-nav .active{color:var(--orange);text-decoration:underline}

/* hero */
.hero{left:0;top:110px;width:1200px;height:539px;background:linear-gradient(135deg,#8a8c8e 0%,#3a3c3f 35%,#1e1f21 60%,#4a4c4f 100%)}
.hero-title{left:0;top:256px;width:1200px;text-align:center;font-family:"Montserrat",sans-serif;font-weight:900;font-size:40px;color:#fff;letter-spacing:1px}
.hero-sub{left:0;top:313px;width:1200px;text-align:center;font-size:19px;color:#fff}
.btn-hero{left:532px;top:370px;width:135px;height:42px;background:var(--orange);color:#fff;font-weight:600;font-size:16px;display:flex;align-items:center;justify-content:center;letter-spacing:.5px}
.dots{left:561px;top:600px;display:flex;gap:11px}
.dots i{width:7px;height:7px;border-radius:50%;background:#fff;display:block}
.dots i.on{background:var(--orange);box-shadow:0 0 0 2px #fff}

/* welcome */
.welcome-art{left:131px;top:734px;width:359px;height:290px;background:linear-gradient(90deg,#f1f1f1 0%,#f1f1f1 45%,#f3d9a6 60%,#e0961c 100%)}
.welcome-divider{left:540px;top:708px;width:1px;height:344px;background:#333}
.eyebrow{left:609px;top:703px;font-size:20px;font-weight:600;color:#444;letter-spacing:1px}
.welcome-title{left:609px;top:730px;font-size:35px;font-weight:700;color:var(--ink);letter-spacing:1px}
.rule{height:3px;background:var(--orange)}
.welcome-text{left:609px;top:820px;width:466px;font-size:15.2px;line-height:23px;color:#444}
.btn-sm{background:var(--orange);color:#fff;font-weight:700;display:flex;align-items:center;justify-content:center;letter-spacing:.3px}

/* sections */
.band{left:0;width:1200px}
.section-title{left:0;width:1200px;text-align:center;font-size:24px;font-weight:700;color:var(--ink);letter-spacing:1px}
.center-rule{left:577px;width:46px}

/* services */
.service-card{width:296px;height:295px;background:#fff;box-shadow:0 2px 8px rgba(0,0,0,.05)}
.service-icon{width:108px;height:108px;border-radius:50%;background:var(--orange);box-shadow:0 4px 8px rgba(0,0,0,.15);display:flex;align-items:center;justify-content:center}
.service-card h3{position:absolute;left:0;width:100%;top:84px;text-align:center;font-size:15px;font-weight:700;color:var(--ink);letter-spacing:.5px}
.service-card .mini{position:absolute;left:133px;top:118px;width:30px;height:2px;background:var(--orange)}
.service-card p{position:absolute;left:40px;width:216px;top:142px;text-align:center;font-size:11px;line-height:16px;color:#444}
.service-card .btn-sm{position:absolute;left:103px;top:235px;width:90px;height:26px;font-size:9.5px}

/* products */
.product-card{width:223px;height:333px;border:1px solid #cfcfcf;background:#fff}
.product-img{position:absolute;left:1px;top:1px;width:219px;height:134px}
.product-card h4{position:absolute;left:0;width:100%;top:158px;text-align:center;font-size:12.5px;font-weight:700;color:var(--ink);letter-spacing:.5px}
.product-card p{position:absolute;left:25px;width:171px;top:185px;text-align:center;font-size:11px;line-height:16px;color:#555}
.price{position:absolute;left:0;width:100%;top:230px;text-align:center;font-family:"Oswald",sans-serif;font-weight:500;font-size:22px;color:var(--orange)}
.btn-outline{position:absolute;left:61px;top:280px;width:94px;height:24px;border:1px solid var(--orange);color:var(--orange);font-size:9.5px;font-weight:700;display:flex;align-items:center;justify-content:center;letter-spacing:.3px}
.arrow{top:1950px}

/* blog */
.blog-img{width:297px;height:216px}
.blog-card{width:270px;height:191px;background:#fff;border-top:3px solid var(--orange);box-shadow:0 3px 8px rgba(0,0,0,.06)}
.blog-card h4{position:absolute;left:25px;top:22px;width:225px;font-size:12px;line-height:15px;font-weight:700;color:var(--ink);letter-spacing:.3px}
.blog-card p{position:absolute;left:25px;top:77px;width:225px;font-size:11.5px;line-height:16px;color:#444}
.blog-card .btn-sm{position:absolute;left:25px;top:136px;width:80px;height:24px;font-size:8.5px}

/* careers */
.careers{left:0;top:2736px;width:1200px;height:398px;background:linear-gradient(100deg,#2a2320 0%,#4a3a30 40%,#5b4334 65%,#3e2f28 100%)}
.careers-title{left:701px;top:2802px;font-size:30px;font-weight:700;color:#fff;letter-spacing:1px}
.careers-text{left:704px;top:2856px;width:330px;font-size:16.5px;line-height:23px;color:#fff}
.career-input{left:708px;top:2926px;width:344px;height:56px;border:3px solid #fff;color:#fff;font-size:13px;font-weight:600;font-style:italic;padding:17px 20px;letter-spacing:.5px}
.career-input svg{position:absolute;right:16px;top:16px}
.btn-search{left:707px;top:3014px;width:125px;height:42px;font-size:15px}

/* footer */
.site-footer{left:0;top:3134px;width:1200px;height:345px;background:var(--footer)}
.footer-head{font-size:13px;font-weight:700;color:#fff;letter-spacing:.5px}
.footer-menu{left:455px;top:3224px;font-size:12px;line-height:20px;color:#fff}
.contact-row{display:flex;gap:10px;align-items:flex-start;color:#fff;font-size:11.5px;line-height:15px}
.ic{width:22px;height:22px;border-radius:50%;background:#fff;flex:none;display:flex;align-items:center;justify-content:center;margin-top:2px}
.footer-line{left:140px;top:3403px;width:920px;height:1px;background:#3a3a3a}
.copyright{left:0;width:1200px;top:3446px;text-align:center;font-size:9.5px;color:#ddd}
</style>
</head>
<body>

<header class="site-header">
  <a class="brand" style="left:131px;top:24px">
    <span class="brand-mark"></span>
    <span class="brand-name">STRATA<small>QATAR</small></span>
  </a>
  <div class="abs search-top">SEARCH FOR ITEMS
    <svg width="12" height="12" viewBox="0 0 12 12"><circle cx="5" cy="5" r="3.5" fill="none" stroke="#222" stroke-width="1.5"/><line x1="7.6" y1="7.6" x2="11" y2="11" stroke="#222" stroke-width="1.5"/></svg>
  </div>
  <a class="abs btn-register">REGISTER</a>
  <div class="abs lang"><span class="flag"></span>EN
    <svg width="8" height="5" viewBox="0 0 8 5" style="margin-left:6px"><path d="M0 0h8L4 5z" fill="#333"/></svg>
  </div>
  <div class="abs cart">MY CART
    <svg width="30" height="28" viewBox="0 0 30 28"><path d="M1 3h5l4 15h15l3-11H8" fill="none" stroke="#333" stroke-width="2"/><circle cx="12" cy="23" r="2.3" fill="#333"/><circle cx="23" cy="23" r="2.3" fill="#333"/></svg>
    <span class="cart-badge">0</span>
  </div>
  <nav class="abs main-nav">
    <a class="active">HOME</a><a>ABOUT US</a><a>PRODUCTS</a><a>SERVICES</a><a>BLOG</a><a>CONTACT US</a>
  </nav>
</header>

<section class="abs hero" role="img" aria-label="Close-up photograph of stacked steel angle bars"></section>
<h1 class="abs hero-title">CONSTRUCTION MATERIAL</h1>
<p class="abs hero-sub">Lorem Ipsum is simply dummy text of the printing</p>
<a class="abs btn-hero">READ MORE</a>
<div class="abs dots"><i></i><i></i><i class="on"></i><i></i><i></i></div>

<div class="abs welcome-art" role="img" aria-label="Line drawing of a house frame with a brick wall and orange roof"></div>
<div class="abs welcome-divider"></div>
<p class="abs eyebrow">WELCOME TO</p>
<h2 class="abs welcome-title">STRATA QATAR</h2>
<div class="abs rule" style="left:609px;top:782px;width:95px"></div>
<p class="abs welcome-text">At vero eos et accusamus et iusto odio dignissimos ducimus qui blanditiis praesentium voluptatum deleniti atque corrupti quos dolores et quas molestias excepturi sint occaecati cupiditate non provident, similique sunt in culpa qui officia deserunt mollitia animi, id est laborum et dolorum fuga. Et harum quidem rerum facilis est et expedita distinctio. Nam libero tempore, cum soluta nobis est eligendi optio cumque nihil impedit quo.</p>
<a class="abs btn-sm" style="left:612px;top:1017px;width:99px;height:31px;font-size:11px">READ MORE</a>

<section class="abs band" style="top:1116px;height:546px;background:var(--soft)"></section>
<h2 class="abs section-title" style="top:1163px">OUR SERVICES</h2>
<div class="abs rule center-rule" style="top:1208px"></div>

<article class="abs service-card" style="left:131px;top:1310px">
  <h3>BUY MATERIALS</h3><span class="mini"></span>
  <p>At vero eos et accusamus et iusto odio dignissimos ducimus qui blanditiis praesentium voluptatum deleniti atque corrupti lorm ipsum.</p>
  <a class="btn-sm">READ MORE</a>
</article>
<article class="abs service-card" style="left:453px;top:1310px">
  <h3>SELL MATERIALS</h3><span class="mini"></span>
  <p>At vero eos et accusamus et iusto odio dignissimos ducimus qui blanditiis praesentium voluptatum deleniti atque corrupti lorm ipsum.</p>
  <a class="btn-sm">READ MORE</a>
</article>
<article class="abs service-card" style="left:773px;top:1310px">
  <h3>HUMAN RESOURCE</h3><span class="mini"></span>
  <p>At vero eos et accusamus et iusto odio dignissimos ducimus qui blanditiis praesentium voluptatum deleniti atque corrupti lorm ipsum.</p>
  <a class="btn-sm">READ MORE</a>
</article>
<div class="abs service-icon" style="left:225px;top:1264px">
  <svg width="54" height="54" viewBox="0 0 54 54" fill="#fff"><rect x="2" y="2" width="14" height="14"/><rect x="20" y="2" width="14" height="14"/><rect x="2" y="20" width="14" height="14"/><rect x="20" y="20" width="14" height="14"/><rect x="38" y="20" width="14" height="14"/><rect x="2" y="38" width="14" height="14"/><rect x="20" y="38" width="14" height="14"/><rect x="38" y="38" width="14" height="14"/></svg>
</div>
<div class="abs service-icon" style="left:546px;top:1264px">
  <svg width="60" height="54" viewBox="0 0 60 54" fill="none" stroke="#fff" stroke-width="3"><path d="M14 22L32 6l18 16"/><path d="M19 18v14h26V18"/><path d="M4 40c8-6 14-6 22-2h12c4 0 4 5 0 5H26"/><path d="M4 40l8 10h20l18-14"/></svg>
</div>
<div class="abs service-icon" style="left:867px;top:1264px">
  <svg width="58" height="58" viewBox="0 0 58 58" fill="none" stroke="#fff" stroke-width="3"><circle cx="29" cy="25" r="16"/><path d="M29 4v5M29 41v5M8 25h5M45 25h5M14 10l4 4M40 36l4 4M44 10l-4 4"/><circle cx="29" cy="22" r="5" fill="#fff"/><path d="M20 36c2-6 16-6 18 0" /><path d="M6 50c8-4 14-4 20-1h10c4 0 4 4 0 4H26"/></svg>
</div>

<h2 class="abs section-title" style="top:1705px">OUR PRODUCTS</h2>
<div class="abs rule center-rule" style="top:1750px"></div>
<svg class="abs arrow" style="left:73px" width="14" height="24" viewBox="0 0 14 24"><path d="M12 2L3 12l9 10" fill="none" stroke="#bbb" stroke-width="2"/></svg>
<svg class="abs arrow" style="left:1099px" width="14" height="24" viewBox="0 0 14 24"><path d="M2 2l9 10-9 10" fill="none" stroke="#bbb" stroke-width="2"/></svg>

<article class="abs product-card" style="left:131px;top:1796px">
  <div class="product-img" role="img" aria-label="Photograph of steel angle bars" style="background:linear-gradient(135deg,#555 0%,#aaa 40%,#333 70%,#ddd 100%)"></div>
  <h4>LOREM IPSUM</h4><p>At vero eos et accusamus et iusto odio dignissimos.</p>
  <div class="price">$ 15.99</div><a class="btn-outline">ADD TO CART</a>
</article>
<article class="abs product-card" style="left:373px;top:1796px">
  <div class="product-img" role="img" aria-label="Photograph of a bundle of steel rebar" style="background:linear-gradient(160deg,#fff 0%,#9a9a9a 45%,#555 65%,#f5f5f5 100%)"></div>
  <h4>LOREM IPSUM</h4><p>At vero eos et accusamus et iusto odio dignissimos.</p>
  <div class="price">$ 25.99</div><a class="btn-outline">ADD TO CART</a>
</article>
<article class="abs product-card" style="left:611px;top:1796px">
  <div class="product-img" role="img" aria-label="Photograph of steel rings and cylinders" style="background:radial-gradient(ellipse at center,#8f8f8f 0%,#c9c9c9 40%,#fff 75%)"></div>
  <h4>LOREM IPSUM</h4><p>At vero eos et accusamus et iusto odio dignissimos.</p>
  <div class="price">$ 35.99</div><a class="btn-outline">ADD TO CART</a>
</article>
<article class="abs product-card" style="left:846px;top:1796px">
  <div class="product-img" role="img" aria-label="Photograph of machined metal parts" style="background:radial-gradient(ellipse at center,#6c6f73 0%,#a7a9ad 40%,#fff 75%)"></div>
  <h4>LOREM IPSUM</h4><p>At vero eos et accusamus et iusto odio dignissimos.</p>
  <div class="price">$ 12.99</div><a class="btn-outline">ADD TO CART</a>
</article>

<section class="abs band" style="top:2181px;height:555px;background:var(--soft)"></section>
<h2 class="abs section-title" style="top:2222px">LATEST BLOG</h2>
<div class="abs rule center-rule" style="top:2267px"></div>

<div class="abs blog-img" style="left:131px;top:2314px;background:linear-gradient(180deg,#3a9a5a 0%,#c8c3bb 45%,#d0603a 75%,#6a6a6a 100%)" role="img" aria-label="Photograph of stacked green and orange pipes in a warehouse"></div>
<div class="abs blog-img" style="left:451px;top:2314px;background:linear-gradient(150deg,#3c3a38 0%,#7a6a5a 50%,#c4a678 100%)" role="img" aria-label="Photograph of a worker cutting wood with a power tool"></div>
<div class="abs blog-img" style="left:770px;top:2314px;background:linear-gradient(160deg,#8e8a86 0%,#c97a4a 55%,#a4502a 100%)" role="img" aria-label="Photograph of a trowel spreading mortar on bricks"></div>

<article class="abs blog-card" style="left:145px;top:2498px">
  <h4>SED UT PERSPICIATIS UNDE OMNIS ISTE NATUS ERROR SIT VOLUPTATEM</h4>
  <p>At vero eos et accusamus et iusto odio dignissimos ducimus qui blanditiis praesentium voluptatum</p>
  <a class="btn-sm">READ MORE</a>
</article>
<article class="abs blog-card" style="left:465px;top:2498px">
  <h4>SED UT PERSPICIATIS UNDE OMNIS ISTE NATUS ERROR SIT VOLUPTATEM</h4>
  <p>At vero eos et accusamus et iusto odio dignissimos ducimus qui blanditiis praesentium voluptatum</p>
  <a class="btn-sm">READ MORE</a>
</article>
<article class="abs blog-card" style="left:784px;top:2498px">
  <h4>SED UT PERSPICIATIS UNDE OMNIS ISTE NATUS ERROR SIT VOLUPTATEM</h4>
  <p>At vero eos et accusamus et iusto odio dignissimos ducimus qui blanditiis praesentium voluptatum</p>
  <a class="btn-sm">READ MORE</a>
</article>

<section class="abs careers" role="img" aria-label="Darkened photograph of a gloved hand laying mortar on a brick wall"></section>
<h2 class="abs careers-title">CAREERS</h2>
<p class="abs careers-text">At vero eos et accusamus et iusto odio digni ssimos ducimus qui blanditiis praesentium.</p>
<div class="abs career-input">ENTER KEYWORD
  <svg width="18" height="18" viewBox="0 0 18 18"><circle cx="7.5" cy="7.5" r="5.5" fill="none" stroke="#fff" stroke-width="2.2"/><line x1="11.5" y1="11.5" x2="16.5" y2="16.5" stroke="#fff" stroke-width="2.2"/></svg>
</div>
<a class="abs btn-sm btn-search">SEARCH</a>

<footer class="abs site-footer"></footer>
<a class="brand" style="left:153px;top:3238px">
  <span class="brand-mark"></span>
  <span class="brand-name" style="color:#fff">STRATA<small>QATAR</small></span>
</a>
<h5 class="abs footer-head" style="left:455px;top:3187px">MENU</h5>
<nav class="abs footer-menu"><div>HOME</div><div>ABOUT US</div><div>PRODUCTS</div><div>SERVICES</div><div>BLOG</div><div>CONTACT US</div></nav>

<h5 class="abs footer-head" style="left:673px;top:3187px">CONTACT US</h5>
<div class="abs contact-row" style="left:672px;top:3226px"><span class="ic"><svg width="10" height="12" viewBox="0 0 10 12"><path d="M5 0a4 4 0 0 0-4 4c0 3 4 8 4 8s4-5 4-8a4 4 0 0 0-4-4z" fill="#222"/><circle cx="5" cy="4" r="1.5" fill="#fff"/></svg></span><span>27 Harbour Row<br>Lusail 40112</span></div>
<div class="abs contact-row" style="left:672px;top:3277px"><span class="ic"><svg width="11" height="11" viewBox="0 0 11 11"><path d="M2 0l2 3-1 1.5c.8 1.6 2 2.8 3.5 3.5L8 7l3 2-1 2C5 11 0 6 0 1z" fill="#222"/></svg></span><span>Call Us<br>555.014.2290</span></div>
<div class="abs contact-row" style="left:672px;top:3327px"><span class="ic"><svg width="11" height="8" viewBox="0 0 11 8"><rect width="11" height="8" fill="#222"/><path d="M0 0l5.5 4.5L11 0" fill="none" stroke="#fff"/></svg></span><span>E mail Us<br>info@strata-market.qa</span></div>

<h5 class="abs footer-head" style="left:969px;top:3187px">FOLLOW US</h5>
<div class="abs contact-row" style="left:970px;top:3226px"><span class="ic"></span><span>Like us on<br>PAGEBOOK</span></div>
<div class="abs contact-row" style="left:970px;top:3276px"><span class="ic"></span><span>Follow us on<br>CHIRPER</span></div>
<div class="abs contact-row" style="left:970px;top:3326px"><span class="ic"></span><span>Follow us on<br>WORKLINK</span></div>

<div class="abs footer-line"></div>
<p class="abs copyright">Copyright © 2020 All Rights Reserved</p>

</body>
</html>
```